Harborline Estates Business Card for Apartment Buildings

Create business cards for resident managers who run apartment buildings. The audience is the public who are searching for apartment rentals, and current residents who live at the apartment building. Key design element will be incorporating the company logo, however, the logo cannot dominate. The building name and manager name are more important than the logo. Current business card design leaves little room for copy, so we may need to reduce the size on the current card to allow for more space for copy.

Target Market(s)

Adults 18-65 years of age, who are looking for an apartment rental, plus current residents who live at our apartment buildings.

Industry/Entity Type

Property Management

Contact Information for Business Card

A major design element will be use of the company logo. Important property and manager contact information must be part of the design. The size of the logo will need to be reduced to make room for building and manager contact copy.

Font styles to use
Sans Serif

Colors
3176b5
000000
959595
ffffff

Requirements
Must have
• 1) Incorporate the company logo.
• 2) Use the company colors (dark blue, black/grey, over white).
• 3) FEATURE THE BUILDING NAME
• 4) FEATURE THE MANAGER NAME
• 5) The company name is less important than BUILDING and MANAGER
• 6) Manager contact information
• **SEE ATTACHED CREATIVE BRIEF**
Nice to have
• 1) Back of card logo watermark
• 2) Ability to write notes on back of carfd
Should not have
• Avoid letting the company logo dominate the card, the building name and manager are more important than the company logo.

```html
<!DOCTYPE html>
<html lang="en">
<head>
<meta charset="utf-8">
<title>Harborline Estates Business Card</title>
<link href="https://fonts.googleapis.com/css2?family=PT+Sans:wght@400;700&display=swap" rel="stylesheet">
<style>
  :root {
    --brand-blue: #1a6aa8;
    --ink-dark: #3f3f42;
    --ink-grey: #555558;
    --rule-grey: #9a9a9a;
    --card-white: #f4f4f4;
    --backdrop: #2a2a2a;
  }
  html, body {
    margin: 0;
    width: 1200px;
    height: 960px;
    overflow: hidden;
    background: var(--backdrop);
    font-family: "PT Sans", Arial, sans-serif;
  }
  .canvas { position: relative; width: 1200px; height: 960px; }
  .card {
    position: absolute;
    width: 600px;
    height: 342px;
    background: var(--card-white);
    box-sizing: border-box;
  }
  .card-front { left: 314px; top: 113px; }
  .card-back { left: 311px; top: 472px; }

  .building-name {
    position: absolute; right: 36px; top: 22px; margin: 0;
    font-size: 39px; font-weight: 700; color: var(--brand-blue);
    white-space: nowrap; letter-spacing: -0.2px;
  }
  .address {
    position: absolute; right: 36px; top: 76px; margin: 0;
    font-size: 14px; line-height: 19px; color: var(--ink-grey); text-align: right;
  }
  .manager { position: absolute; right: 36px; top: 145px; text-align: right; }
  .manager-name { margin: 0; font-size: 21px; font-weight: 700; color: var(--brand-blue); line-height: 24px; }
  .manager-title { margin: 0; font-size: 14px; font-weight: 700; color: var(--ink-dark); line-height: 18px; }

  .contact-list {
    position: absolute; right: 36px; top: 219px; margin: 0; padding: 0; list-style: none;
  }
  .contact-list li {
    display: flex; justify-content: flex-end; align-items: center;
    height: 19.5px; font-size: 13.5px; color: var(--ink-grey);
  }
  .contact-list svg { width: 14px; height: 14px; margin-left: 9px; fill: var(--brand-blue); }

  .company-mark-front {
    position: absolute; left: 44px; top: 150px;
    display: flex; align-items: flex-start; gap: 12px;
  }
  .mark-square { width: 26px; height: 26px; background: var(--brand-blue); flex: none; margin-top: 6px; }
  .company-name-front {
    margin: 0; font-size: 32px; line-height: 36px; font-weight: 700; color: var(--ink-dark); width: 200px;
  }

  .company-mark-back {
    position: absolute; left: 0; right: 0; top: 58px;
    display: flex; justify-content: center; align-items: center; gap: 10px;
  }
  .company-mark-back .mark-square { margin-top: 0; width: 22px; height: 22px; }
  .company-name-back { margin: 0; font-size: 30px; font-weight: 700; color: var(--brand-blue); }

  .note-line {
    position: absolute; left: 39px; width: 521px; height: 0;
    border-top: 1.5px solid var(--rule-grey);
  }
</style>
</head>
<body>
<div class="canvas">

  <section class="card card-front">
    <div class="company-mark-front">
      <span class="mark-square"></span>
      <p class="company-name-front">Harborline Estates</p>
    </div>

    <h1 class="building-name">Linden Grove Apartments</h1>
    <p class="address">1284 Keller Avenue<br>Brookton, CA 92870</p>

    <div class="manager">
      <p class="manager-name">Marisol Vega</p>
      <p class="manager-title">Resident Manager</p>
    </div>

    <ul class="contact-list">
      <li>555-201-4830
        <svg viewBox="0 0 16 16" aria-hidden="true"><path d="M3.5 1l3 3-1.6 1.8c.9 2 2.4 3.5 4.3 4.4L11 8.5l3 3-2 2.4C6.8 13.3 2.7 9.2 1.5 3z"/></svg>
      </li>
      <li>555-318-7742
        <svg viewBox="0 0 16 16" aria-hidden="true"><path d="M4.5 0h7a1 1 0 0 1 1 1v14a1 1 0 0 1-1 1h-7a1 1 0 0 1-1-1V1a1 1 0 0 1 1-1zm.8 2v10.5h5.4V2zM8 13.3a.9.9 0 1 0 0 1.8.9.9 0 0 0 0-1.8z"/></svg>
      </li>
      <li>555-644-2019
        <svg viewBox="0 0 16 16" aria-hidden="true"><path d="M4 1h8v4H4zM1 6h14v7h-3v2H4v-2H1zm4 5v3h6v-3z"/></svg>
      </li>
      <li>marisol@harborlineest.com
        <svg viewBox="0 0 16 16" aria-hidden="true"><path d="M1 3h14v10H1zm1.5 1.3v.4L8 8.8l5.5-4.1v-.4zm0 2.1v5.3h11V6.4L8 10.5z"/></svg>
      </li>
      <li>www.harborlineest.com
        <svg viewBox="0 0 16 16" aria-hidden="true"><path d="M8 1a7 7 0 1 0 0 14A7 7 0 0 0 8 1zm-2 3.5c1 0 1.6.8 1.2 1.6-.4.7-1.6.6-1.8 1.6-.2 1 .9 1.4.5 2.4-.4.8-1.5.4-2-.6-.6-1.3-.2-3.4.8-4.3.4-.4.8-.7 1.3-.7zm4.5 1.2c.9.2 1.8 1 1.6 2.2-.2 1-1 .9-1.4 1.8-.4.9.3 2-.7 2.4-.8.3-1.3-.8-1.1-1.8.2-1.2-.9-1.6-.6-2.8.2-.9 1.4-1.9 2.2-1.8z"/></svg>
      </li>
    </ul>
  </section>

  <section class="card card-back">
    <div class="company-mark-back">
      <span class="mark-square"></span>
      <p class="company-name-back">Harborline Estates</p>
    </div>
    <div class="note-line" style="top:161px"></div>
    <div class="note-line" style="top:209px"></div>
    <div class="note-line" style="top:257px"></div>
    <div class="note-line" style="top:305px"></div>
  </section>

</div>
</body>
</html>
```